Modern Business Card

Modern professional business card with more than just logo and demographic info. Something memorable.

We are a trendy/modern chiropractic group with an emphasis on neurology, hence the minimalist-type brain logo. We want to convey that modern and technical aspect with professionalism and the elite nature of our practice environment.

```html
<!DOCTYPE html>
<html lang="en">
<head>
<meta charset="utf-8">
<title>Clarity Chiropractic – Business Card</title>
<link href="https://fonts.googleapis.com/css2?family=Crimson+Pro:wght@400;500&family=Titillium+Web:wght@400;600&display=swap" rel="stylesheet">
<style>
  :root {
    --backdrop: #d8cdbf;
    --card-white: #ffffff;
    --card-black: #050a10;
    --ink: #1c1c1c;
    --ink-soft: #4a4a4a;
    --accent: #5a84bb;
    --grey-type: #7d7d7d;
    --light-type: #f2f2f2;
  }
  * { margin: 0; padding: 0; box-sizing: border-box; }
  html, body { width: 1200px; height: 859px; overflow: hidden; }
  body { background: var(--backdrop); position: relative; font-family: "Titillium Web", sans-serif; }

  .card {
    position: absolute;
    top: 288px;
    width: 502px;
    height: 285px;
    overflow: hidden;
    box-shadow: 0 6px 16px rgba(0,0,0,0.25);
  }
  .card--front { left: 59px; background: var(--card-white); }
  .card--back { left: 639px; background: linear-gradient(160deg, #141b24 0%, var(--card-black) 60%); }

  .wordmark { font-family: "Crimson Pro", serif; line-height: 1; }
  .wordmark__name { display: block; font-weight: 500; letter-spacing: 0.5px; }
  .wordmark__sub { display: block; font-weight: 400; letter-spacing: 0.6px; }

  .card--front .wordmark { position: absolute; left: 29px; top: 34px; color: var(--ink); }
  .card--front .wordmark__name { font-size: 30px; }
  .card--front .wordmark__sub { font-size: 16px; color: var(--ink-soft); margin-top: -3px; }

  .person { position: absolute; left: 29px; top: 124px; }
  .person__name { font-family: "Crimson Pro", serif; font-size: 19px; color: var(--ink-soft); letter-spacing: 0.4px; line-height: 1.1; }
  .person__title { font-size: 13.5px; color: var(--accent); line-height: 1.3; }

  .divider { position: absolute; left: 29px; top: 180px; width: 149px; height: 1.5px; background: var(--ink); }

  .contacts { position: absolute; left: 29px; top: 196px; list-style: none; }
  .contacts li { display: flex; align-items: center; gap: 6px; font-size: 13px; color: var(--ink-soft); height: 17px; }
  .contacts svg { width: 12px; height: 12px; flex: none; }
  .contacts strong { color: var(--accent); font-weight: 600; }

  .accent-band { position: absolute; top: 0; width: 30px; height: 285px; background: var(--accent); }
  .card--front .accent-band { left: 462px; }
  .card--back .accent-band { left: 8px; }

  .card--back .lockup { position: absolute; left: 193px; top: 112px; display: flex; align-items: center; gap: 10px; }
  .lockup__mark { width: 40px; height: 40px; background: var(--accent); }
  .card--back .wordmark { color: var(--light-type); }
  .card--back .wordmark__name { font-size: 38px; }
  .card--back .wordmark__sub { font-size: 20px; color: var(--grey-type); margin-top: -5px; }
</style>
</head>
<body>
  <section class="card card--front" aria-label="Card front">
    <div class="wordmark">
      <span class="wordmark__name">CLARITY</span>
      <span class="wordmark__sub">CHIROPRACTIC</span>
    </div>
    <div class="person">
      <p class="person__name">EVAN MARLOWE</p>
      <p class="person__title">Training Specialist</p>
    </div>
    <div class="divider"></div>
    <ul class="contacts">
      <li><svg viewBox="0 0 12 12" aria-hidden="true"><circle cx="6" cy="6" r="5.2" fill="none" stroke="#1f4f8f" stroke-width="1"/><path d="M4 3.3l1 1.2-.6.7a4 4 0 0 0 2.4 2.4l.7-.6 1.2 1-.7.8C6 8.6 3.4 6 3.2 4z" fill="#1f4f8f"/></svg>555.014.2387</li>
      <li><svg viewBox="0 0 12 12" aria-hidden="true"><rect x="1" y="2.5" width="10" height="7" fill="none" stroke="#1f4f8f" stroke-width="1"/><path d="M1 2.5l5 4 5-4" fill="none" stroke="#1f4f8f" stroke-width="1"/></svg>e.marlowe@claritychiro.com</li>
      <li><svg viewBox="0 0 12 12" aria-hidden="true"><circle cx="6" cy="6" r="5.2" fill="#1f4f8f"/><path d="M1 6h10M6 .8v10.4M6 .8c-3 3-3 7.4 0 10.4M6 .8c3 3 3 7.4 0 10.4" fill="none" stroke="#fff" stroke-width=".7"/></svg>www.<strong>claritychiro</strong>.com</li>
    </ul>
    <div class="accent-band"></div>
  </section>

  <section class="card card--back" aria-label="Card back">
    <div class="accent-band"></div>
    <div class="lockup">
      <div class="lockup__mark"></div>
      <div class="wordmark">
        <span class="wordmark__name">CLARITY</span>
        <span class="wordmark__sub">CHIROPRACTIC</span>
      </div>
    </div>
  </section>
</body>
</html>
```